Graphic Insert - For Pillow Case

We are purchasing new pillow cases for a campaign we are running and need a graphic insert as part of our corporate branding and product description to go in our packaging. The packaging will be a clear plastic back with this graphic insert.

Size of Flyer: 6"x9"

Description: 440 Thread Count Egyptian Cotton Pillow Cases
Quantity: 2
Size of Pillow Case: Standard
Descriptive Words: Soft, Caress, Smooth, Gentle

Our website: www.velardo.com

Thanks,

Dale

```html
<!DOCTYPE html>
<html lang="en">
<head>
<meta charset="utf-8">
<title>Velardo Pillow Case Insert</title>
<link href="https://fonts.googleapis.com/css2?family=Arimo&display=swap" rel="stylesheet">
<style>
  :root {
    --bg: #d0d1bd;
    --ring-outer: #abae8d;
    --ring-inner: #a0a47f;
    --ring-edge: #f4f4ec;
    --ink-grey: #6c6d6b;
    --ink-white: #ffffff;
  }
  html, body {
    margin: 0;
    padding: 0;
    width: 800px;
    height: 1200px;
    overflow: hidden;
    background: var(--bg);
  }
  .insert {
    position: relative;
    width: 800px;
    height: 1200px;
    background: var(--bg);
    font-family: "Arimo", Arial, sans-serif;
  }
  .brand {
    position: absolute;
    left: 0;
    top: 130px;
    width: 800px;
    text-align: center;
  }
  .brand-name {
    font-family: "Arimo", Arial, sans-serif;
    font-weight: 400;
    font-size: 72px;
    line-height: 84px;
    color: var(--ink-grey);
  }
  .product-badge {
    position: absolute;
    left: 0;
    top: 0;
  }
  .product-details {
    position: absolute;
    left: 0;
    width: 800px;
    top: 545px;
    text-align: center;
    color: var(--ink-white);
    font-size: 35px;
    line-height: 42px;
  }
  .product-details p { margin: 0; }
  .product-details .gap { margin-top: 48px; }
  .descriptors {
    position: absolute;
    top: 1104px;
    left: 0;
    width: 800px;
    height: 40px;
    color: var(--ink-grey);
    font-size: 32px;
  }
  .descriptors span {
    position: absolute;
    transform: translateX(-50%);
  }
</style>
</head>
<body>
<main class="insert">
  <header class="brand">
    <div class="brand-name">Velardo</div>
  </header>

  <svg class="product-badge" width="800" height="1200" viewBox="0 0 800 1200" aria-hidden="true">
    <circle cx="400" cy="681" r="344" fill="var(--ring-outer)" stroke="var(--ring-edge)" stroke-width="6"/>
    <circle cx="400" cy="681" r="287" fill="var(--ring-inner)"/>
  </svg>

  <section class="product-details">
    <p>440 Thread Count</p>
    <p>Egyptian Cotton Pillow Cases</p>
    <p class="gap">Quantity: 2</p>
    <p class="gap">Size of Pillow Case: Standard</p>
  </section>

  <footer class="descriptors">
    <span style="left:219px">Smooth</span>
    <span style="left:420px">Gentle</span>
    <span style="left:602px">Soft</span>
  </footer>
</main>
</body>
</html>
```